Web Site for Strategy and Technology Consulting Company

We are looking for a website design that engages potential customers to understand our services and contact us. In this contest, we are looking for a homepage design, but the winning designer will be favored for the design of some of the more complicated interior pages of the site. An additional contest (or contests) for these pages will be added soon.

PLATROM AND RESPONSIVE DESIGN
The site will be implemented in WordPress using the Elementor page builder.
We are looking for a design that will look good on phones are well as laptop browsers.

UPLOADED FILES INCLUDE:
1a A wireframe of the homepage we are looking for. The Uploaded PDF also includes a draft of the text proposed for the homepage. Designers are free to go beyond the wireframe, but all elements of the wireframe should be included.
1b A Word document with the draft text of the homepage.
2a-d The Norvalith logo. Two versions are included – a dark version which works well against a light background, and a light version which works well against a dark background.
3 The Norvalith color palette with HEX and RGB values. Designers are not limited to this palette, but colors should be complementary.
4 A draft of the homepage menu
5 Service sheets with information on the services we provide

MORE ABOUT NORVALITH
Norvalith is a consulting company focused on transforming businesses through software. Our tagline, “Transformation Delivered,” recognizes the gap business often have between business transformation and the software they end up with. By listening to our customers and understanding their vision and where they are, we help get our customers where they want to go.

We increase our capability by working with many consultants and partners, allowing us to provide our customers with the best people and the software that best suits them.

Industry/Entity Type

Consulting

Number of Pages Required

1 page

Font styles to use
Sans Serif

Requirements
Must have
• the content represented on the wireframe uploaded
Nice to have
• interactive features, such as roll-over icons that reveal additional information

```html
<!DOCTYPE html>
<html lang="en">
<head>
<meta charset="utf-8">
<title>Norvalith — Transformation Delivered</title>
<link href="https://fonts.googleapis.com/css2?family=Outfit:wght@300;400;500;600;700;800&display=swap" rel="stylesheet">
<style>
:root{
  --blue:#2b63a6;
  --blue-deep:#23548f;
  --yellow:#f2c300;
  --ink:#1c1c1c;
  --text:#3a3a3a;
  --muted:#9a9a9a;
  --header:#dcdcdc;
  --footer:#232323;
  --white:#ffffff;
}
*{box-sizing:border-box;margin:0;padding:0}
html,body{width:1200px;height:4286px;overflow:hidden;background:var(--white)}
body{font-family:"Outfit",sans-serif;color:var(--text);position:relative}
.section{position:absolute;left:0;width:1200px}
.abs{position:absolute}
.photo{position:absolute}
h2.title{position:absolute;font-weight:800;color:var(--ink);line-height:1.05;letter-spacing:.3px}
.copy{position:absolute;font-size:12px;line-height:1.55;color:var(--text)}
.bullets{position:absolute;list-style:none}
.bullets li{position:relative;padding-left:30px;font-size:12px;line-height:1.6;color:var(--text)}
.bullets li::before{content:"";position:absolute;left:0;top:4px;width:10px;height:10px;border:2px solid var(--blue);background:#7ea6d6}
.bullets.yellow li::before{border-color:var(--yellow);background:#fff}
.lead-link{position:absolute;color:var(--blue);font-weight:600;font-size:15.5px;line-height:1.45}

/* header */
.site-header{top:0;height:92px;background:var(--header)}
.brand{position:absolute;font-weight:400;letter-spacing:.5px}
.brand-dot{display:inline-block;width:8px;height:8px;border-radius:50%;background:var(--blue);margin-right:6px;vertical-align:middle}
.site-header .brand{left:125px;top:22px;font-size:38px;color:#4b4b4b}
.nav a{position:absolute;top:37px;font-size:13px;color:#2a2a2a;text-decoration:none}
.contact-btn{position:absolute;left:905px;top:22px;width:170px;height:45px;background:var(--blue);color:#fff;font-size:12.5px;font-weight:600;display:flex;align-items:center;justify-content:center}
.contact-btn::after{content:"";position:absolute;right:8px;top:6px;width:6px;height:6px;background:var(--yellow)}

/* cards */
.service-card{position:absolute;width:142px;height:175px;background:#fff;box-shadow:0 2px 10px rgba(0,0,0,.1);text-align:center;padding-top:30px}
.service-card.active{background:var(--blue);color:#fff}
.service-card svg{display:block;margin:0 auto 6px}
.service-card h3{font-size:11px;font-weight:700;color:var(--ink);line-height:1.3;padding:0 10px}
.service-card.active h3{color:#fff}
.service-card p{font-size:9.5px;line-height:1.45;color:#555;padding:3px 14px 0}
.service-card.active p{color:#e6eefb}

.cta-band{position:absolute;left:630px;top:1475px;width:570px;height:78px;background:var(--yellow);color:var(--blue);font-weight:600;font-size:13.5px;text-align:right;padding:15px 47px 0 0;line-height:1.7}

.stars{position:absolute;color:var(--yellow);font-size:17px;letter-spacing:6px}
.round-btn{position:absolute;width:56px;height:56px;border-radius:50%;display:flex;align-items:center;justify-content:center}
.round-btn.blue{background:var(--blue)}
.round-btn.yellow{background:var(--yellow);width:56px;height:56px}

.tech-card{position:absolute;width:302px;height:355px;background:#fff;box-shadow:0 4px 14px rgba(0,0,0,.15);padding:12px}
.tech-card .photo{position:static;width:100%;height:100%}
.tech-label{position:absolute;top:3697px;font-size:21px;font-weight:500;text-align:center;width:302px}

/* footer */
.site-footer{top:3800px;height:486px;background:var(--footer);color:#fff}
.site-footer .brand{left:125px;top:85px;font-size:60px;color:#fff}
.contact-item{position:absolute;left:125px;display:flex;align-items:center;font-size:12.5px;color:#ddd;line-height:1.6}
.contact-item .ring{width:52px;height:52px;border-radius:50%;border:2px solid #bbb;display:flex;align-items:center;justify-content:center;margin-right:18px;flex:none}
.foot-col{position:absolute;top:140px}
.foot-col h4{font-size:17px;font-weight:700;margin-bottom:18px}
.foot-col a{display:block;font-size:13.5px;color:#eee;text-decoration:none;margin-bottom:29px}
.copyright{position:absolute;right:130px;top:320px;font-size:12px;color:#ddd}
.social{position:absolute;top:366px;width:28px;height:28px;border-radius:50%;background:var(--yellow)}
</style>
</head>
<body>

<header class="section site-header">
  <div class="brand"><span class="brand-dot"></span>Norvalith</div>
  <nav class="nav">
    <a style="left:422px" href="#">About Us</a>
    <a style="left:530px" href="#">Services</a>
    <a style="left:632px" href="#">Insights</a>
    <a style="left:730px" href="#">Join Us</a>
  </nav>
  <div class="contact-btn">Contact Us</div>
</header>

<section class="section" style="top:92px;height:741px">
  <div class="photo" role="img" aria-label="Smiling consultant in glasses seated at a desk with a laptop" style="left:0;top:0;width:600px;height:741px;background:linear-gradient(135deg,#e9e6e2 0%,#cfd3c8 45%,#8f9f86 70%,#dcd8d2 100%)"></div>
  <h2 class="title" style="left:658px;top:98px;font-size:53px">Transformation<br>Delivered</h2>
  <p class="copy" style="left:658px;top:236px;width:410px">We Do More For Our Customers Than Implement Software. We Listen. We Work To Understand Where They Are In Their Transformation Journey And Where They Want To Go. We Partner With Them To Clear The Roadblocks That Stand In Their Way, Ensuring They Reach Their Destination. At Norvalith, We:</p>
  <ul class="bullets" style="left:658px;top:382px;width:410px">
    <li style="margin-bottom:20px">Focus On Business Value, With An Emphasis On Delivering Value Quickly.</li>
    <li style="margin-bottom:20px">Meet Our Customers Where They Are Without Backing Them Up To The Beginning Of Their Journey.</li>
    <li style="margin-bottom:20px">Provide A Wide Range Of Services, From Strategy To Product Support.</li>
    <li>Commit To Our Customer's Long-Term Success.</li>
  </ul>
  <p class="lead-link" style="left:658px;top:618px">Norvalith Is Business Transformation, Delivered.</p>
</section>

<section class="section" style="top:833px;height:742px">
  <h2 class="title" style="left:125px;top:66px;font-size:40px">Transformation<br>Supported By<br>Technology</h2>
  <p class="copy" style="left:125px;top:220px;width:420px;font-size:10.5px">During Our Early Years, Norvalith Focused Only On Business Transformation. We Came To Realize That Successful Transformation Often Depended On Quality Software Implementations, And Often More Than One. Now We Focus On Five Things, The Five Things Most Businesses Need To Reach Their Goals.</p>
  <div class="photo" role="img" aria-label="Team collaborating at a desk with a keyboard, tablet and phone" style="left:600px;top:0;width:600px;height:742px;background:linear-gradient(135deg,#e2a635 0%,#f0c653 35%,#e8e4dc 65%,#d7d2c9 100%)"></div>
</section>

<div class="service-card active" style="left:125px;top:1163px">
  <svg width="26" height="26" viewBox="0 0 26 26"><rect x="5" y="3" width="12" height="16" fill="var(--yellow)"/><rect x="3" y="19" width="20" height="4" fill="var(--yellow)"/></svg>
  <h3>Business Transformation</h3><p>Define And Execute Your Strategy</p>
</div>
<div class="service-card" style="left:277px;top:1163px;padding-top:22px">
  <svg width="26" height="26" viewBox="0 0 26 26"><circle cx="13" cy="13" r="10" fill="none" stroke="var(--yellow)" stroke-width="4" stroke-dasharray="5 3"/><circle cx="13" cy="13" r="4" fill="var(--yellow)"/></svg>
  <h3>ERP Implementations</h3><p>Assess, Upgrade, And Implement ERP Solutions To Meet Your Needs</p>
</div>
<div class="service-card" style="left:430px;top:1163px;padding-top:22px">
  <svg width="26" height="26" viewBox="0 0 26 26"><circle cx="10" cy="10" r="7" fill="var(--yellow)"/><path d="M16 16l6 6" stroke="var(--yellow)" stroke-width="3"/></svg>
  <h3>CRM Implementations</h3><p>Define And Execute Your Strategy</p>
</div>
<div class="service-card" style="left:125px;top:1350px;padding-top:30px">
  <svg width="26" height="22" viewBox="0 0 26 22"><rect x="2" y="2" width="22" height="18" fill="none" stroke="var(--yellow)" stroke-width="2"/><rect x="6" y="10" width="3" height="7" fill="var(--yellow)"/><rect x="12" y="7" width="3" height="10" fill="var(--yellow)"/><rect x="18" y="12" width="3" height="5" fill="var(--yellow)"/></svg>
  <h3>BI And Data</h3><p>Assess, Upgrade, And Implement ERP Solutions To Meet Your Needs</p>
</div>
<div class="service-card" style="left:277px;top:1350px;padding-top:26px">
  <svg width="26" height="26" viewBox="0 0 26 26"><circle cx="10" cy="10" r="7" fill="var(--yellow)"/><circle cx="19" cy="17" r="4" fill="var(--yellow)"/></svg>
  <h3>Building The Right Team Of People</h3><p>Hire Resources For Your Transformation Journey</p>
</div>

<div class="cta-band">Find Out How Norvalith Can Help You Put All The<br>Pieces Together And Get Them Done.</div>

<section class="section" style="top:1575px;height:742px">
  <div class="photo" role="img" aria-label="Portrait of a consultant in glasses" style="left:0;top:0;width:195px;height:742px;background:linear-gradient(160deg,#6b4a3a,#b98a72 50%,#5a4a48)"></div>
  <div class="photo" role="img" aria-label="Portrait of a smiling consultant" style="left:200px;top:0;width:200px;height:742px;background:linear-gradient(160deg,#3a2a22,#c49a7e 50%,#7a6a64)"></div>
  <div class="photo" role="img" aria-label="Portrait of a smiling male consultant" style="left:405px;top:0;width:195px;height:742px;background:linear-gradient(160deg,#4a3a30,#c89c80 50%,#9fb2c8)"></div>
  <h2 class="title" style="left:658px;top:172px;font-size:40px">It's The People</h2>
  <p class="copy" style="left:658px;top:240px;width:415px;font-size:10.5px">The World Has Changed In The Past Twenty Years. The People You Need Might Not All Work For One Company. Our Clients Want The Best Resources, Available Quickly. That's Why, In Addition To Our Team Of Experts, We Partner With:</p>
  <ul class="bullets yellow" style="left:658px;top:355px;width:415px">
    <li style="margin-bottom:20px">A Large Network Of Expert Consultants Who Are The Best At What They Do,</li>
    <li>Service Providers All Over The World To Provide The Resources And Value That Are Right For You, Available 24 X 7.</li>
  </ul>
  <p class="lead-link" style="left:658px;top:494px;width:420px">People Are Invariably At The Center Of Our Customer's Success. Find Out How We Can Add Our Experts To Yours.</p>
</section>

<section class="section" style="top:2317px;height:741px">
  <h2 class="title" style="left:125px;top:143px;font-size:40px">Testimonials</h2>
  <p class="abs" style="left:125px;top:228px;font-size:20px;font-weight:700;color:var(--blue)">Daniel Reyes</p>
  <p class="abs" style="left:125px;top:263px;font-size:11.5px;color:var(--muted)">Business Name</p>
  <p class="copy" style="left:125px;top:312px;width:390px;font-size:11.5px">Lorem Ipsum is simply dummy text of the printing and typesetting industry. Lorem Ipsum has been the industry's standard dummy text ever since the 1500s, when an unknown printer took a galley of type and scrambled it to make a type specimen book. It has survived not only five centuries, but also the leap into electronic typesetting, remaining essentially unchanged.</p>
  <div class="stars" style="left:125px;top:461px">★★★★★</div>
  <div class="round-btn blue" style="left:125px;top:533px"><svg width="24" height="14" viewBox="0 0 24 14"><path d="M23 7H2M8 1L2 7l6 6" fill="none" stroke="#fff" stroke-width="1.8"/></svg></div>
  <div class="round-btn blue" style="left:214px;top:533px"><svg width="24" height="14" viewBox="0 0 24 14"><path d="M1 7h21M16 1l6 6-6 6" fill="none" stroke="#fff" stroke-width="1.8"/></svg></div>
  <div class="photo" role="img" aria-label="Smiling woman in warm golden outdoor light" style="left:600px;top:0;width:600px;height:741px;background:radial-gradient(circle at 60% 45%,#e8b070 0%,#c47a2e 40%,#6b3d14 100%)"></div>
</section>

<section class="section" style="top:3058px;height:742px">
  <div class="photo" role="img" aria-label="Blue-tinted office background with charts" style="left:0;top:0;width:600px;height:742px;background:linear-gradient(180deg,#3a74b8,var(--blue-deep))"></div>
  <h2 class="title" style="left:685px;top:98px;font-size:40px">Technologies</h2>
  <div class="round-btn yellow" style="left:685px;top:164px"><svg width="12" height="16" viewBox="0 0 12 16"><path d="M9 2L3 8l6 6" fill="none" stroke="var(--blue)" stroke-width="3"/></svg></div>
  <div class="round-btn yellow" style="left:762px;top:164px"><svg width="12" height="16" viewBox="0 0 12 16"><path d="M3 2l6 6-6 6" fill="none" stroke="var(--blue)" stroke-width="3"/></svg></div>
</section>

<div class="tech-card" style="left:125px;top:3313px"><div class="photo" role="img" aria-label="Hands typing on a laptop showing an order dashboard" style="background:linear-gradient(160deg,#c9cdd2,#6f767e 55%,#2e3338)"></div></div>
<div class="tech-card" style="left:448px;top:3313px"><div class="photo" role="img" aria-label="Laptop with sales charts and a smartphone on a desk" style="background:linear-gradient(160deg,#d8dadc,#8a9096 55%,#3c4045)"></div></div>
<div class="tech-card" style="left:772px;top:3313px"><div class="photo" role="img" aria-label="Hands on a keyboard with glowing marketing icons" style="background:linear-gradient(160deg,#9fb6d6,#45608f 55%,#1d2a48)"></div></div>
<p class="tech-label" style="left:125px;color:#fff">Order Processing</p>
<p class="tech-label" style="left:448px;top:3690px;background:linear-gradient(90deg,#fff 0 50%,var(--ink) 50% 100%);-webkit-background-clip:text;background-clip:text;color:transparent">Sales Automation</p>
<p class="tech-label" style="left:772px;top:3690px;color:var(--ink)">Marketing Automation</p>

<footer class="section site-footer">
  <div class="brand"><span class="brand-dot" style="width:12px;height:12px"></span>Norvalith</div>
  <div class="contact-item" style="top:187px"><span class="ring"><svg width="16" height="16" viewBox="0 0 24 24"><path d="M6 3l3 0 2 5-2 1.5a11 11 0 0 0 5.5 5.5L16 13l5 2v3a2 2 0 0 1-2 2A17 17 0 0 1 4 5a2 2 0 0 1 2-2z" fill="#fff"/></svg></span>(555) 204-8817</div>
  <div class="contact-item" style="top:262px"><span class="ring"><svg width="16" height="12" viewBox="0 0 16 12"><rect width="16" height="12" rx="1" fill="#fff"/><path d="M1 1l7 6 7-6" fill="none" stroke="#232323" stroke-width="1.4"/></svg></span>hello@norvalith.com</div>
  <div class="contact-item" style="top:354px"><span class="ring"><svg width="14" height="18" viewBox="0 0 14 18"><path d="M7 0a7 7 0 0 1 7 7c0 5-7 11-7 11S0 12 0 7a7 7 0 0 1 7-7z" fill="#fff"/><circle cx="7" cy="7" r="2.5" fill="#232323"/></svg></span>480 Harborview Plaza Suite<br>210, Lakeport, MN 55012</div>
  <div class="foot-col" style="left:517px">
    <h4>Links</h4>
    <a href="#">Home</a><a href="#">About Us</a><a href="#">Services</a><a href="#">Insights</a><a href="#">Join Us</a>
  </div>
  <div class="foot-col" style="left:692px">
    <h4>Company</h4>
    <a href="#">Community</a><a href="#">Blog</a><a href="#">Forums</a><a href="#">Meetups</a>
  </div>
  <p class="copyright">© Copyright 2023 Norvalith</p>
  <span class="social" style="left:908px"></span>
  <span class="social" style="left:953px"></span>
  <span class="social" style="left:998px"></span>
  <span class="social" style="left:1043px"></span>
</footer>

</body>
</html>
```